Crumb Joy pastry business card design

I need a logo and a business card design for my baking business, "Crumb Joy". I daily bake French pastries from scratch using high quality ingredients and directly cater to local customers. My product is very authentic but sold at a casual setting . I'm looking for a simple, cute, stylish yet earthy design. Like this kind of feel:
http://clipvista.example/71946302
Target Market(s)
Metropolitan food conscious consumers in their 20-40s
Industry/Entity Type
Business
Requirements
Must have
- Soft pastel colors or other types of color schemes that would remind French pastries.
email: welovecrumbles@mailnest.example
twitter@bitemesf
www.crumbjoyla.example
Nice to have
Should not have
- pictures of pastries - sketches are ok.

```html
<!DOCTYPE html>
<html lang="en">
<head>
<meta charset="utf-8">
<title>Crumb Joy Pastries – Business Card</title>
<link rel="stylesheet" href="https://fonts.googleapis.com/css2?family=Open+Sans:wght@400;600&display=swap">
<style>
  :root {
    --backdrop: #2b2b2b;
    --card-glow: #6b2a2f;
    --card-mid: #4e1418;
    --card-edge: #340407;
    --brand-brown: #2a120c;
    --tagline-grey: #c9c4c4;
    --label-red: #e0262c;
    --detail-white: #f4f1f1;
  }
  html, body {
    margin: 0;
    padding: 0;
    width: 1200px;
    height: 900px;
    overflow: hidden;
    background: var(--backdrop);
  }
  .canvas {
    position: relative;
    width: 1200px;
    height: 900px;
    display: flex;
    align-items: center;
    justify-content: center;
  }
  .business-card {
    position: relative;
    width: 840px;
    height: 480px;
    background: radial-gradient(ellipse 60% 65% at 45% 45%, var(--card-glow) 0%, var(--card-mid) 50%, var(--card-edge) 100%);
    font-family: "Open Sans", Arial, sans-serif;
  }
  .brand {
    position: absolute;
    left: 0;
    right: 0;
    top: 150px;
    text-align: center;
  }
  .brand-name {
    margin: 0;
    font-size: 92px;
    font-weight: 600;
    line-height: 1;
    color: var(--brand-brown);
    letter-spacing: 1px;
  }
  .brand-tagline {
    margin: 14px 0 0;
    font-size: 30px;
    font-weight: 400;
    letter-spacing: 22px;
    padding-left: 22px;
    color: var(--tagline-grey);
  }
  .contact {
    position: absolute;
    right: 40px;
    bottom: 40px;
    display: grid;
    grid-template-columns: auto auto;
    column-gap: 14px;
    font-size: 17px;
    line-height: 1.15;
  }
  .contact-label {
    text-align: right;
    color: var(--label-red);
  }
  .contact-value {
    color: var(--detail-white);
  }
</style>
</head>
<body>
  <main class="canvas">
    <section class="business-card">
      <div class="brand">
        <h1 class="brand-name">Crumb Joy</h1>
        <p class="brand-tagline">PASTRIES</p>
      </div>
      <div class="contact">
        <span class="contact-label">email:</span>
        <span class="contact-value">welovecrumbles@mailnest.example</span>
        <span class="contact-label">twitter:</span>
        <span class="contact-value">twitter@crumbjoyla</span>
        <span class="contact-label">website:</span>
        <span class="contact-value">www.crumbjoyla.example</span>
      </div>
    </section>
  </main>
</body>
</html>
```